Online Sports Booking Business

We need a flyer design for a new company based in Bahrain called "GoalSlotter.com".

GoalSlotter is an online booking service for the sport field in Bahrain. We would like to design a flyer in away that reflects our idea and the type of customers who will benefit from the service. You can visit the website in order to get an idea about the service provided.

Service Description:
Simply sign up, search and choose, book and pay for any sports venue or activity using your own computer or smartphone.

- Choose from different sport centers and activities in Bahrain
- Compare based on unbiased reviews by real people
- Check for availability
- Book and pay online in less than a minute
- Track, manage, modify and cancel your bookings online
- Receive automatic notifications (upon request) whenever your favorite venue/activity is available
- Rate and post reviews about your experience

We would like the design to use the color green as a background, nice and casual visual icons and images to show the above steps. The final design should communicate the value and benefits in a joyful and casual way that is attractive to the sport lovers.
Updates

Project Deadline Extended
Reason: I need interested designers to take part in this project.

Target Market(s)

english speakers aged 18-45 who are into sports.

Industry/Entity Type

Computer

Font styles to use
Sans Serif
Other font styles liked:
• something similar to the logo

Colors
add136
9bcb3c
ffffff

Requirements
Must have
• Please use the content in the attachment. Logo can be taken from goalslotter.example
Nice to have
• steps and benefits to use icons and visual presentations rather than dull text only.

```html
<!DOCTYPE html>
<html lang="en">
<head>
<meta charset="utf-8">
<title>GoalSlotter.com – Services</title>
<link rel="stylesheet" href="https://fonts.googleapis.com/css2?family=Anton&family=Questrial&display=swap">
<style>
  :root {
    --bar-dark: #2a2a2a;
    --brand-green: #add136;
    --brand-green-2: #9bcb3c;
    --grass-light: #6fbf2e;
    --grass-dark: #2f7a12;
    --title-green: #3d6a14;
    --ink: #111111;
    --white: #ffffff;
    --stripe: rgba(255, 255, 255, 0.82);
  }
  html, body {
    margin: 0;
    padding: 0;
    width: 849px;
    height: 1200px;
    overflow: hidden;
    background: var(--white);
  }
  .flyer {
    position: relative;
    width: 849px;
    height: 1200px;
    overflow: hidden;
    font-family: "Questrial", sans-serif;
  }
  .top-bar {
    position: absolute;
    left: 0; top: 0;
    width: 849px; height: 146px;
    background: var(--bar-dark);
  }
  .brand {
    position: absolute;
    left: 38px; top: 42px;
    display: flex;
    align-items: center;
    gap: 14px;
  }
  .brand-dot {
    width: 44px; height: 44px;
    border: 4px solid var(--white);
    border-radius: 50%;
    box-sizing: border-box;
  }
  .brand-name {
    color: var(--white);
    font-size: 40px;
    line-height: 1;
    letter-spacing: 0.5px;
  }
  .brand-tagline {
    position: absolute;
    left: 104px; top: 87px;
    color: var(--brand-green);
    font-size: 16px;
    font-weight: 700;
    letter-spacing: 0.3px;
  }
  .field {
    position: absolute;
    left: 0; top: 146px;
    width: 849px; height: 946px;
    background: radial-gradient(ellipse at 70% 20%, var(--grass-light), var(--grass-dark) 85%);
  }
  .field-line {
    position: absolute;
    left: 0; top: 146px;
    width: 849px; height: 946px;
  }
  .sports-balls {
    position: absolute;
    left: 626px; top: 248px;
    width: 223px; height: 850px;
    border-radius: 110px 0 0 110px;
    background: linear-gradient(180deg, #f2f2f2 0%, #c9c9c9 16%, #a8552a 32%, #8e4220 44%, #eeeeee 58%, #d8e23a 72%, #c9d52b 82%, #f4f4f4 100%);
    opacity: 0.95;
  }
  .services-title {
    position: absolute;
    left: 134px; top: 170px;
    margin: 0;
    font-family: "Anton", sans-serif;
    font-weight: 400;
    font-size: 78px;
    letter-spacing: 1px;
    color: var(--title-green);
    -webkit-text-stroke: 1.5px #1f3f08;
  }
  .service-list {
    list-style: none;
    margin: 0; padding: 0;
  }
  .service-item {
    position: absolute;
    left: 118px;
    display: flex;
    align-items: center;
    gap: 14px;
    transform: translateY(-50%);
  }
  .service-icon {
    width: 70px; height: 62px;
    flex: none;
  }
  .service-label {
    font-size: 27px;
    color: var(--ink);
    letter-spacing: 0.2px;
  }
  .bottom-bar {
    position: absolute;
    left: 0; top: 1092px;
    width: 849px; height: 108px;
    background: var(--bar-dark);
    display: flex;
    align-items: center;
    justify-content: center;
    gap: 40px;
    color: var(--white);
    font-size: 27px;
  }
  .contact {
    display: flex;
    align-items: center;
    gap: 12px;
  }
  .contact svg { width: 26px; height: 26px; }
</style>
</head>
<body>
<div class="flyer">
  <header class="top-bar">
    <div class="brand">
      <span class="brand-dot"></span>
      <span class="brand-name">GoalSlotter.com</span>
    </div>
    <div class="brand-tagline">Online Pitch Booking</div>
  </header>

  <div class="field" role="img" aria-label="Close-up of green grass turf"></div>
  <svg class="field-line" viewBox="0 0 849 946" aria-hidden="true">
    <polygon points="112,0 578,0 578,946 58,946" fill="var(--stripe)"/>
  </svg>
  <div class="sports-balls" role="img" aria-label="Stack of sports balls: football, basketball, baseball, tennis ball and golf ball"></div>

  <h1 class="services-title">Services</h1>

  <ul class="service-list">
    <li class="service-item" style="top:318px">
      <svg class="service-icon" viewBox="0 0 70 62">
        <rect x="4" y="6" width="62" height="40" rx="3" fill="var(--ink)"/>
        <rect x="9" y="11" width="52" height="30" fill="var(--white)"/>
        <g stroke="var(--ink)" stroke-width="2"><line x1="15" y1="18" x2="18" y2="18"/><line x1="22" y1="18" x2="54" y2="18"/><line x1="15" y1="25" x2="18" y2="25"/><line x1="22" y1="25" x2="54" y2="25"/><line x1="15" y1="32" x2="18" y2="32"/><line x1="22" y1="32" x2="54" y2="32"/></g>
        <rect x="30" y="46" width="10" height="8" fill="var(--ink)"/>
        <rect x="20" y="54" width="30" height="4" rx="2" fill="var(--ink)"/>
      </svg>
      <span class="service-label">Choose your pitch</span>
    </li>
    <li class="service-item" style="top:417px">
      <svg class="service-icon" viewBox="0 0 70 62">
        <path d="M8 44 Q2 50 4 58 Q12 54 16 48" fill="var(--white)" stroke="var(--ink)" stroke-width="3"/>
        <ellipse cx="26" cy="36" rx="20" ry="14" fill="var(--white)" stroke="var(--ink)" stroke-width="3"/>
        <ellipse cx="42" cy="24" rx="22" ry="16" fill="var(--white)" stroke="var(--ink)" stroke-width="3"/>
        <circle cx="33" cy="24" r="3" fill="var(--ink)"/><circle cx="42" cy="24" r="3" fill="var(--ink)"/><circle cx="51" cy="24" r="3" fill="var(--ink)"/>
      </svg>
      <span class="service-label">Review and compare</span>
    </li>
    <li class="service-item" style="top:520px">
      <svg class="service-icon" viewBox="0 0 70 62">
        <rect x="6" y="8" width="58" height="50" rx="5" fill="var(--ink)"/>
        <rect x="12" y="20" width="46" height="32" fill="var(--white)"/>
        <rect x="18" y="2" width="5" height="12" rx="2" fill="var(--ink)"/>
        <rect x="47" y="2" width="5" height="12" rx="2" fill="var(--ink)"/>
        <g fill="var(--ink)"><rect x="16" y="24" width="8" height="6"/><rect x="27" y="24" width="8" height="6"/><rect x="38" y="24" width="8" height="6"/><rect x="16" y="33" width="8" height="6"/><rect x="38" y="33" width="8" height="6"/><rect x="49" y="33" width="6" height="6"/><rect x="16" y="42" width="8" height="6"/><rect x="27" y="42" width="8" height="6"/><rect x="38" y="42" width="8" height="6"/></g>
      </svg>
      <span class="service-label">Check for availability</span>
    </li>
    <li class="service-item" style="top:633px">
      <svg class="service-icon" viewBox="0 0 70 62">
        <rect x="4" y="24" width="44" height="34" fill="var(--white)" stroke="var(--ink)" stroke-width="2.5"/>
        <circle cx="22" cy="42" r="8" fill="none" stroke="var(--ink)" stroke-width="2"/>
        <text x="22" y="47" text-anchor="middle" font-size="13" font-family="Questrial, sans-serif" fill="var(--ink)">$</text>
        <path d="M30 30 L48 8 L64 18 L56 30 L44 34 Z" fill="var(--ink)"/>
      </svg>
      <span class="service-label">Book and pay</span>
    </li>
    <li class="service-item" style="top:750px">
      <svg class="service-icon" viewBox="0 0 70 62">
        <path d="M10 30 A25 25 0 0 1 56 16" fill="none" stroke="var(--ink)" stroke-width="5"/>
        <polygon points="50,8 62,14 54,24" fill="var(--ink)"/>
        <path d="M60 32 A25 25 0 0 1 14 46" fill="none" stroke="var(--ink)" stroke-width="5"/>
        <polygon points="20,54 8,48 16,38" fill="var(--ink)"/>
        <circle cx="33" cy="29" r="10" fill="var(--white)" stroke="var(--ink)" stroke-width="4"/>
        <line x1="40" y1="36" x2="48" y2="44" stroke="var(--ink)" stroke-width="5" stroke-linecap="round"/>
      </svg>
      <span class="service-label">Track and manage</span>
    </li>
    <li class="service-item" style="top:867px">
      <svg class="service-icon" viewBox="0 0 70 62">
        <rect x="4" y="18" width="50" height="36" rx="3" fill="var(--ink)"/>
        <polyline points="6,20 29,40 52,20" fill="none" stroke="var(--white)" stroke-width="2.5"/>
        <circle cx="54" cy="16" r="11" fill="var(--ink)" stroke="var(--white)" stroke-width="2"/>
        <text x="54" y="21" text-anchor="middle" font-size="14" font-family="Questrial, sans-serif" fill="var(--white)">3</text>
      </svg>
      <span class="service-label">Get notified</span>
    </li>
    <li class="service-item" style="top:993px">
      <svg class="service-icon" viewBox="0 0 70 62">
        <ellipse cx="36" cy="28" rx="28" ry="24" fill="var(--ink)"/>
        <path d="M14 44 L6 60 L26 50 Z" fill="var(--ink)"/>
        <path d="M24 28 H30 V42 H24 Z M32 28 L38 16 Q42 14 42 20 L40 26 H48 Q52 27 50 32 L47 40 Q46 42 43 42 H32 Z" fill="var(--white)"/>
      </svg>
      <span class="service-label">Rate and comment</span>
    </li>
  </ul>

  <footer class="bottom-bar">
    <span class="contact">
      <svg viewBox="0 0 24 24"><path d="M6.6 10.8a15.1 15.1 0 0 0 6.6 6.6l2.2-2.2a1 1 0 0 1 1-.25 11.4 11.4 0 0 0 3.6.57 1 1 0 0 1 1 1V20a1 1 0 0 1-1 1A17 17 0 0 1 3 4a1 1 0 0 1 1-1h3.5a1 1 0 0 1 1 1c0 1.25.2 2.45.57 3.6a1 1 0 0 1-.25 1z" fill="var(--brand-green-2)"/></svg>
      +973-35550147
    </span>
    <span class="contact">
      <svg viewBox="0 0 24 24"><rect x="2" y="5" width="20" height="14" rx="1" fill="none" stroke="var(--brand-green-2)" stroke-width="2"/><polyline points="3,6 12,13 21,6" fill="none" stroke="var(--brand-green-2)" stroke-width="2"/></svg>
      support@goalslotter.example
    </span>
  </footer>
</div>
</body>
</html>
```